Massage Certificate Design that is Elegant, Modern, Hip with a "Pop"

We need a massage certificate for our Chiropractic office. Our brand feel is modern, clean, hip, and bold. Something that has some "pop" to it and that is different. We play dance music on Fridays, we care for kids and families, and provide vitality care, not just about neck and back pain. We would like to see a design that incorporates our logo along with a burnt orange accent color, tan, white, and black. We attached a sample certificate. On one side we would like to have it designate the massage price of $50, a space to write in who the certificate is for, who it is from, a space to write in an expiration date. On the back of the certificate we would like to have the office contact info. 4173 W. Marlow Lane, C204, Scottsdale, AZ 85260. A map of the location.
Phone: (480) 731-2946
Facebook
Twitter

Target Market(s)

Moms, Wellness Minded, Vitality Focused, Looking for reducing stress and muscle stiffness

Industry/Entity Type

Health And Wellness

Colors
f37122
000000
fefefe

Requirements
Must have
• Burnt orange accent color, tan, black, and white colors used.

```html
<!DOCTYPE html>
<html lang="en">
<head>
<meta charset="utf-8">
<title>Massage Certificate – Camelback Family Chiropractic</title>
<link href="https://fonts.googleapis.com/css2?family=Lato:wght@400;700&family=Saira:wght@600;700&family=Oswald:wght@600&display=swap" rel="stylesheet">
<style>
  :root{
    --orange:#f37122;
    --orange-deep:#e8611a;
    --orange-light:#f6893f;
    --black:#000000;
    --white:#fefefe;
    --grey:#a9a9a9;
    --tan:#d9cbb6;
    --ink:#1a1a1a;
    --canvas:#e9e6e2;
  }
  *{margin:0;padding:0;box-sizing:border-box}
  html,body{width:1200px;height:900px;overflow:hidden}
  body{background:var(--canvas);position:relative;font-family:"Lato",sans-serif}

  .card{position:absolute;left:83px;width:1034px;height:388px;background:var(--white);overflow:hidden;box-shadow:0 4px 14px rgba(0,0,0,.25)}
  .card--front{top:50px}
  .card--back{top:473px}
  .card__shapes{position:absolute;inset:0}

  /* front */
  .spine-art{position:absolute;left:95px;top:120px;width:250px;height:200px;border-radius:40px;
    background:radial-gradient(ellipse at center,rgba(210,210,210,.45),rgba(255,255,255,0) 70%)}
  .brand{position:absolute;color:var(--ink);font-family:"Lato",sans-serif;font-weight:400;text-transform:uppercase;line-height:1.2}
  .brand__dot{display:inline-block;width:12px;height:12px;border-radius:50%;background:var(--ink);margin-bottom:6px}
  .brand--front{left:95px;top:250px;font-size:15px;letter-spacing:.5px}
  .brand--back{left:880px;top:330px;font-size:11px;text-align:right}

  .title{position:absolute;left:340px;top:18px;width:660px;text-align:center;font-family:"Saira",sans-serif;font-weight:700;font-size:52px;letter-spacing:1px;
    background:linear-gradient(#ffffff 0%,#e4e4e4 50%,#a8a8a8 55%,#d8d8d8 100%);-webkit-background-clip:text;background-clip:text;color:transparent}
  .fields{position:absolute;left:342px;top:125px;width:676px;color:#fde7d8;font-size:20px}
  .fields__lead{color:var(--white);font-weight:700;margin-bottom:6px}
  .field{display:flex;align-items:flex-end;height:33px}
  .field__line{flex:1;border-bottom:2px solid #2a1a10;margin-left:8px;margin-bottom:5px}
  .price{position:absolute;left:355px;top:300px;font-family:"Saira",sans-serif;font-weight:600;font-size:50px;color:var(--orange);letter-spacing:.5px}
  .price__amount{color:var(--white);font-weight:700}

  /* back */
  .map{position:absolute;left:17px;top:92px;width:362px;height:200px;border-radius:16px;background:linear-gradient(135deg,#e6e2dc,#d8d3cb);box-shadow:0 3px 8px rgba(0,0,0,.3)}
  .spine-faint{position:absolute;left:490px;top:95px;width:540px;height:140px;border-radius:70px;background:radial-gradient(ellipse at center,rgba(200,212,222,.45),rgba(255,255,255,0) 70%)}
  .contact{position:absolute;left:565px;top:112px;width:335px;text-align:center}
  .contact__tag{display:inline-block;background:var(--ink);color:var(--orange);font-family:"Oswald",sans-serif;font-weight:600;font-size:28px;padding:0 18px;height:38px;line-height:38px;border-radius:10px;box-shadow:0 3px 6px rgba(0,0,0,.35)}
  .contact__address{margin-top:22px;font-size:20px;color:var(--ink);line-height:26px}
  .contact__phone{font-weight:700;display:inline-flex;align-items:center;gap:4px}
  .social{position:absolute;top:333px;display:block;width:34px;height:33px;border-radius:5px;box-shadow:0 1px 3px rgba(0,0,0,.3)}
  .social--one{left:475px;background:linear-gradient(#7fd0ee,#3aa4d6)}
  .social--two{left:517px;background:linear-gradient(#5c7fc4,#3b5998)}
</style>
</head>
<body>

<section class="card card--front">
  <svg class="card__shapes" width="1034" height="388" viewBox="0 0 1034 388">
    <defs>
      <linearGradient id="orangeFill" x1="0" y1="0" x2="1" y2="0">
        <stop offset="0" stop-color="#f6893f"/><stop offset=".5" stop-color="#f37122"/><stop offset="1" stop-color="#e8611a"/>
      </linearGradient>
    </defs>
    <path d="M258,0 H280 C330,70 336,190 318,295 L300,300 C314,190 306,80 258,0Z" fill="#a9a9a9"/>
    <path d="M276,0 H1034 V295 H318 C336,190 330,70 276,0Z" fill="url(#orangeFill)"/>
    <path d="M238,388 C282,350 302,300 312,240 C316,270 318,285 322,295 H1034 V388Z" fill="#000"/>
  </svg>
  <div class="spine-art" role="img" aria-label="Faint spine illustration behind the logo"></div>
  <div class="brand brand--front"><span class="brand__dot"></span><br>Camelback Family<br>Chiropractic</div>

  <h1 class="title">MASSAGE CERTIFICATE</h1>
  <div class="fields">
    <p class="fields__lead">Certificate is for</p>
    <div class="field"><span>Name</span><span class="field__line"></span></div>
    <div class="field"><span>From</span><span class="field__line"></span></div>
    <div class="field"><span>Expiration date</span><span class="field__line"></span></div>
  </div>
  <p class="price">Massage price of <span class="price__amount">$50</span></p>
</section>

<section class="card card--back">
  <svg class="card__shapes" width="1034" height="388" viewBox="0 0 1034 388">
    <defs>
      <linearGradient id="orangeBack" x1="0" y1="0" x2="1" y2="0">
        <stop offset="0" stop-color="#f37122"/><stop offset="1" stop-color="#f6893f"/>
      </linearGradient>
    </defs>
    <path d="M470,0 C420,90 405,250 470,388 H485 C420,250 435,90 490,0Z" fill="#a9a9a9"/>
    <path d="M0,0 H458 C408,90 395,250 455,388 H0Z" fill="url(#orangeBack)"/>
  </svg>
  <div class="map" role="img" aria-label="Street map showing the office location"></div>
  <div class="spine-faint" role="img" aria-label="Faint spine illustration"></div>

  <div class="contact">
    <span class="contact__tag">OFFICE CONTACT INFO</span>
    <p class="contact__address">4173 W. Marlow Lane,<br>C204, Scottsdale, AZ 85260<br>
      <span class="contact__phone">
        <svg width="16" height="18" viewBox="0 0 24 24" aria-hidden="true"><path d="M6.6 10.8a15 15 0 0 0 6.6 6.6l2.2-2.2a1 1 0 0 1 1-.25 11.4 11.4 0 0 0 3.6.57 1 1 0 0 1 1 1V20a1 1 0 0 1-1 1A17 17 0 0 1 3 4a1 1 0 0 1 1-1h3.5a1 1 0 0 1 1 1c0 1.25.2 2.45.57 3.57a1 1 0 0 1-.25 1z" fill="#f37122"/></svg>(480) 731-2946
      </span>
    </p>
  </div>

  <span class="social social--one" role="img" aria-label="Social profile link"></span>
  <span class="social social--two" role="img" aria-label="Social profile link"></span>

  <div class="brand brand--back"><span class="brand__dot"></span><br>Camelback Family<br>Chiropractic</div>
</section>

</body>
</html>
```